Stories from Elm trifold brochure design

We are a start up company that will help seniors write their memoirs...beginning with a few ancestors and their heritage and continuing through their own history...how they would like to be remembered in the next generation. I envision a senior citizen at an older writing desk, writing her memoirs, with a book (maybe standing on top, leaning slightly) that has the words Stories from Elm.com on the back binding. OR maybe a senior couple walking into the sunset with the same book somewhere in the frame. Communicating the relevance of every life being significant to those that come after them...when a genealogy doesn't say enough about the details of one's life. Please note that I am open to the professionals own ideas...I am not locked into my concepts. I would like one or two phrases..."When A Genealogy Doesn't Say Enough" and/or "Every life legacy is a gift for the next generation to treasure" to be in the design.
A few documents are loaded that contain notes for our web designers. Maybe they will help you with our thoughts.

Reason: We have added some additional photos that might be useful.

Target Market(s)

Seniors and the baby boomer generation

Industry/Entity Type

Graphic Design

Requirements
Must have
• Stories from Elm
• Doris Whitcombe, M.A.
• 1-609-382-5171 (local)
• 1-866-4TALEKP (toll free)
• info@storiesfromelm.com
• storiesfromelm.com
Should not have
• Scripts that would be challenging for seniors to read.

```html
<!DOCTYPE html>
<html lang="en">
<head>
<meta charset="utf-8">
<title>Stories from Elm – Trifold Brochure Inside</title>
<link href="https://fonts.googleapis.com/css2?family=Noto+Serif:ital,wght@0,400;0,700;1,400;1,700&family=Cabin:ital,wght@0,400;0,500;0,600;1,400&family=Caveat:wght@500&display=swap" rel="stylesheet">
<style>
  :root{
    --page:#ffffff;
    --panel:#ede8e2;
    --gold:#b59b5a;
    --gold-soft:#d8c99c;
    --brown:#4a2f22;
    --ink:#3d2a20;
    --card:#f5f3e4;
    --shadow:rgba(0,0,0,.25);
  }
  *{margin:0;padding:0;box-sizing:border-box}
  html,body{width:1200px;height:1000px;overflow:hidden;background:var(--page)}
  .brochure{position:absolute;left:57px;top:82px;width:1088px;height:840px;background:var(--page);box-shadow:0 2px 8px var(--shadow);overflow:hidden}
  .abs{position:absolute}

  /* left panel */
  .intro{left:0;top:0;width:358px;height:840px;background:var(--panel);font-family:"Noto Serif",serif;color:var(--ink)}
  .intro-brush{left:14px;top:8px;width:340px;height:100px}
  .intro-question{left:12px;top:18px;width:322px;text-align:right;font-family:"Noto Serif",serif;font-style:italic;color:var(--gold);font-size:16px;line-height:27px}
  .intro-question .big{font-family:"Caveat",cursive;font-size:29px;font-style:normal}
  .intro-question .mark{font-family:"Noto Serif",serif;font-size:40px;font-style:normal;font-weight:700;vertical-align:-4px}
  .intro-lead{left:27px;top:122px;width:310px;font-weight:700;font-size:15.5px;line-height:21px;color:var(--brown)}
  .intro-body{left:27px;width:315px;font-size:13.6px;line-height:19.7px;text-align:justify;letter-spacing:-.25px}
  .intro-sub{left:27px;top:443px;font-weight:700;font-style:italic;font-size:15px;color:var(--brown)}

  /* right side */
  .help-title{left:383px;top:30px;font-family:"Noto Serif",serif;font-weight:700;font-style:italic;font-size:21px;color:var(--brown)}
  .help-title .script{font-family:"Caveat",cursive;font-weight:500;font-style:normal;font-size:32px;color:var(--ink)}
  .help-rule{left:380px;top:64px;width:265px;height:3px;background:linear-gradient(90deg,var(--gold),var(--gold-soft) 80%,transparent)}
  .tagline{left:614px;top:34px;width:270px;text-align:center;font-family:"Noto Serif",serif;font-style:italic;font-size:15.5px;line-height:20px;color:#7a6a50}
  .step-head{left:384px;font-family:"Noto Serif",serif;font-weight:700;font-size:15.5px;color:var(--brown)}
  .badge{width:36px;height:36px;border-radius:50%;background:var(--gold);color:#fff;font-family:"Cabin",sans-serif;font-size:24px;display:flex;align-items:center;justify-content:center}
  .option{left:426px;width:272px;font-family:"Cabin",sans-serif;font-weight:600;font-size:14.5px;line-height:20px;color:var(--brown)}
  .pkg-label{left:384px;font-family:"Cabin",sans-serif;font-weight:500;font-size:17px;color:var(--gold)}
  .pkg-card{left:383px;width:323px;border-radius:16px;background:var(--card)}
  .pkg-num{left:0;top:0}
  .pkg-name{left:42px;top:4px;font-family:"Cabin",sans-serif;font-weight:500;font-size:19.5px;color:var(--brown)}
  .pkg-icon{left:5px;top:42px}
  .pkg-list{left:111px;top:34px;width:190px;list-style:none;font-family:"Cabin",sans-serif;font-weight:600;font-size:13.5px;line-height:19px;color:var(--brown)}
  .pkg-list li{position:relative;padding-left:22px}
  .pkg-list li::before{content:"";position:absolute;left:0;top:6px;width:7px;height:7px;border-radius:50%;background:var(--brown)}

  .note{left:750px;width:275px;font-family:"Cabin",sans-serif;font-weight:500;font-size:14.5px;line-height:20px;color:var(--brown);padding-left:26px}
  .note b{font-weight:700}
  .note svg{position:absolute;left:0;top:2px}
  .contact{left:777px;top:516px;width:202px;height:67px;border-radius:14px;background:var(--card);padding:11px 16px;font-family:"Cabin",sans-serif;font-weight:600;font-size:15px;line-height:22px;color:var(--brown)}
  .photo{border-radius:50%}
  .brand{left:900px;top:740px;font-family:"Noto Serif",serif;font-size:20px;color:var(--gold);display:flex;align-items:center;gap:8px}
  .brand-dot{width:10px;height:10px;border-radius:50%;background:var(--gold)}
</style>
</head>
<body>
<div class="brochure">

  <section class="abs intro">
    <svg class="abs intro-brush" viewBox="0 0 340 100" aria-hidden="true"><path d="M20 14 C120 6 260 4 338 8 L330 94 C240 98 120 96 10 86 Z" fill="#ffffff" opacity=".85"/></svg>
    <p class="abs intro-question">If you were alive in <span class="big">100 years,</span><br>what would you <span class="big">share</span> with your<br><span class="big">descendants</span><span class="mark">?</span></p>
    <p class="abs intro-lead">Now you have a vehicle to help you <em>immortalize</em> your thoughts for the future…specifically for those who will want to know!</p>
    <p class="abs intro-body" style="top:216px">We are not all presidents of countries or CEO’s of fortune 500 companies! But “every life legacy is a gift to be treasured by the next generation.”</p>
    <p class="abs intro-body" style="top:296px">Does your family host generations of soldiers, doctors, farmers, scientists, mechanics, entrepreneurs, writers, politicians, contractors, pastors, artisans, athletes, musicians, etc..? Generational patterns can often emerge when writing your story that will interest the next generation.</p>
    <p class="abs intro-sub">When a genealogy isn’t enough!</p>
    <p class="abs intro-body" style="top:478px">A genealogy, while very relevant, doesn’t offer the personal story of the names we find. A biography can place a deeper relevance on the face for future descendants. Every life is a legacy to pass forward and we at Stories from Elm believe everyone should chronicle their life journey in writing. This commitment allows you to be remembered for who you truly are as a person.</p>
    <p class="abs intro-body" style="top:675px">Think about it….Do you know the triumphs and tribulations of your ancestors? Do you wish you did? Well, so will those falling into your personal family tree.</p>
  </section>

  <h2 class="abs help-title">How we can <span class="script">help</span></h2>
  <div class="abs help-rule"></div>
  <p class="abs tagline">We offer several unique packages to best suit your needs.</p>

  <div class="abs photo" role="img" aria-label="Photo of three generations seated on a bench outdoors with dogs" style="left:891px;top:-30px;width:196px;height:196px;background:radial-gradient(circle at 50% 30%,#c9dbea,#8aa35a 70%,#6f8a3e)"></div>
  <div class="abs photo" role="img" aria-label="Photo of a senior woman writing at an old desk by lamplight" style="left:727px;top:102px;width:196px;height:196px;background:radial-gradient(circle at 40% 40%,#e3a367,#9a5a2e 60%,#4a2514)"></div>
  <div class="abs photo" role="img" aria-label="Photo of a family holding hands on the beach at sunset" style="left:931px;top:168px;width:195px;height:195px;background:radial-gradient(circle at 40% 55%,#fff2cf,#c9a777 45%,#5a4a3a)"></div>

  <h3 class="abs step-head" style="top:94px">First, choose an option:</h3>
  <div class="abs badge" style="left:380px;top:127px">A</div>
  <p class="abs option" style="top:122px">You can provide the majority of input in an organized fashion (as specified by Stories from Elm), OR</p>
  <div class="abs badge" style="left:380px;top:198px">B</div>
  <p class="abs option" style="top:203px">We help organize photos and interview one-on-one for history, OR</p>
  <div class="abs badge" style="left:380px;top:266px">C</div>
  <p class="abs option" style="top:263px">Bring friends together for a 12 week program so we can help you on your way.</p>

  <h3 class="abs step-head" style="top:320px">Next, choose a package:</h3>

  <p class="abs pkg-label" style="top:345px">Package</p>
  <div class="abs pkg-card" style="top:371px;height:122px">
    <div class="abs badge pkg-num">1</div>
    <h4 class="abs pkg-name">Standard Portrait Book</h4>
    <svg class="abs pkg-icon" width="95" height="56" viewBox="0 0 95 56" aria-hidden="true">
      <rect x="1" y="1" width="93" height="54" fill="#fff" stroke="#3f5f8f" stroke-width="2"/><line x1="47" y1="1" x2="47" y2="55" stroke="#3f5f8f"/>
      <rect x="6" y="6" width="36" height="44" fill="#cfe3f0"/><circle cx="16" cy="14" r="7" fill="#86bfe0"/>
      <rect x="52" y="7" width="36" height="3" fill="#a8cbe2"/><rect x="52" y="14" width="36" height="3" fill="#a8cbe2"/><rect x="52" y="21" width="36" height="3" fill="#a8cbe2"/><rect x="70" y="32" width="18" height="16" fill="#a8d3ec"/>
    </svg>
    <ul class="abs pkg-list"><li>Up to 120 pages</li><li>8” x 10”</li><li>Include photos and text throughout</li></ul>
  </div>

  <p class="abs pkg-label" style="top:503px">Package</p>
  <div class="abs pkg-card" style="top:530px;height:120px">
    <div class="abs badge pkg-num">2</div>
    <h4 class="abs pkg-name">Standard Trade Book</h4>
    <svg class="abs pkg-icon" width="95" height="60" viewBox="0 0 95 60" aria-hidden="true">
      <rect x="1" y="1" width="93" height="58" fill="#fff" stroke="#8a5a9a" stroke-width="2"/><line x1="47" y1="1" x2="47" y2="59" stroke="#8a5a9a"/>
      <rect x="8" y="8" width="18" height="14" fill="#d9c2de"/><circle cx="28" cy="40" r="9" fill="#dfb0e6"/>
      <g fill="#d9c2de"><rect x="52" y="7" width="36" height="3"/><rect x="52" y="14" width="36" height="3"/><rect x="52" y="21" width="36" height="3"/><rect x="52" y="28" width="36" height="3"/><rect x="52" y="35" width="36" height="3"/><rect x="52" y="42" width="36" height="3"/></g>
    </svg>
    <ul class="abs pkg-list" style="width:165px"><li>Up to 250 pages, or 100,000 words</li><li>6” x 9”</li><li>Few photos, mainly text</li></ul>
  </div>

  <p class="abs pkg-label" style="top:660px">Package</p>
  <div class="abs pkg-card" style="top:686px;height:120px">
    <div class="abs badge pkg-num">3</div>
    <h4 class="abs pkg-name">Standard Portrait Book</h4>
    <svg class="abs pkg-icon" width="95" height="56" viewBox="0 0 95 56" aria-hidden="true">
      <rect x="1" y="1" width="93" height="54" fill="#fff" stroke="#e07a3a" stroke-width="2"/><line x1="47" y1="1" x2="47" y2="55" stroke="#e07a3a"/>
      <rect x="6" y="6" width="36" height="44" fill="#fde6cc"/><circle cx="16" cy="14" r="7" fill="#f8cf9c"/>
      <rect x="52" y="7" width="36" height="3" fill="#f6c99a"/><rect x="52" y="14" width="36" height="3" fill="#f6c99a"/><rect x="52" y="21" width="36" height="3" fill="#f6c99a"/><rect x="70" y="32" width="18" height="16" fill="#f8cf9c"/>
    </svg>
    <ul class="abs pkg-list"><li>with 120 to 200 pages</li><li>8” x 10”</li><li>Include photos and text throughout</li></ul>
  </div>

  <p class="abs note" style="top:376px"><svg width="16" height="16" viewBox="0 0 16 16" aria-hidden="true"><path d="M1 1 L15 8 L1 15 Z" fill="var(--gold)"/></svg>All publications will also be available as an <b>ebook</b>.</p>
  <p class="abs note" style="top:437px"><svg width="16" height="16" viewBox="0 0 16 16" aria-hidden="true"><path d="M1 1 L15 8 L1 15 Z" fill="var(--gold)"/></svg>Call or email us to schedule a <b>free consultation</b> individually or as a group today.</p>
  <div class="abs contact">1-609-382-5171<br>info@storiesfromelm.com</div>
  <p class="abs note" style="top:605px"><svg width="16" height="16" viewBox="0 0 24 24" aria-hidden="true"><path d="M12 1 L15 9 L23 9 L17 14 L19 23 L12 18 L5 23 L7 14 L1 9 L9 9 Z" fill="var(--gold)"/></svg>Ask about <b>available financing</b> if needed. We are committed to your legacy!</p>

  <div class="abs brand"><span class="brand-dot"></span>Stories from Elm</div>
</div>
</body>
</html>
```